Property development & Investment company Need a logo & business card design

Our name is KT Estates Australia Pty Ltd
Need logo & business card design

Target Market(s)

People dealing in commercial property

Industry/Entity Type

Business

Contact Information for Business Card

KT Estates Australia
Peter Dunmore Mobile0419 703 646
Email Peter@quillbarrow.com.au

Font styles to use
Sans Serif

Requirements
Must have
• company name
• contact details
Nice to have
• KT Estates Bold
• Australia Not Bold
Should not have
• To busy of a look

```html
<!DOCTYPE html>
<html lang="en">
<head>
<meta charset="utf-8">
<title>KT Estates Australia – Business Card</title>
<link rel="stylesheet" href="https://fonts.googleapis.com/css2?family=Montserrat:wght@400;500&display=swap">
<style>
  :root {
    --backdrop: #e6e6e6;
    --card: #ffffff;
    --rust: #b04a2e;
    --ink: #1c1c1c;
  }
  * { margin: 0; padding: 0; box-sizing: border-box; }
  html, body {
    width: 1200px;
    height: 1200px;
    overflow: hidden;
    background: var(--backdrop);
    font-family: "Montserrat", sans-serif;
  }
  .business-card {
    position: absolute;
    left: 120px;
    top: 318px;
    width: 960px;
    height: 563px;
    background: var(--card);
    overflow: hidden;
  }
  .brand {
    position: absolute;
    left: 103px;
    top: 84px;
    display: flex;
    align-items: center;
    gap: 18px;
  }
  .brand-square {
    width: 46px;
    height: 46px;
    background: var(--rust);
  }
  .brand-name {
    color: var(--rust);
    font-weight: 500;
    font-size: 38px;
    letter-spacing: 0.2px;
    white-space: nowrap;
  }
  .divider {
    position: absolute;
    left: 0;
    top: 179px;
    width: 100%;
    height: 5px;
    background: var(--rust);
  }
  .contact {
    position: absolute;
    left: 541px;
    top: 208px;
    color: var(--ink);
  }
  .contact-name {
    font-weight: 500;
    font-size: 35px;
    line-height: 1;
    margin-left: 5px;
    margin-bottom: 20px;
  }
  .contact-line {
    font-weight: 400;
    font-size: 23px;
    line-height: 1;
    margin-bottom: 17px;
    white-space: nowrap;
  }
</style>
</head>
<body>
  <div class="business-card">
    <div class="brand">
      <span class="brand-square" aria-hidden="true"></span>
      <span class="brand-name">KT Estates Australia</span>
    </div>
    <div class="divider"></div>
    <div class="contact">
      <p class="contact-name">Peter Dunmore</p>
      <p class="contact-line">Mobile: 0438 512 907</p>
      <p class="contact-line">Email: Peter@quillbarrow.com.au</p>
    </div>
  </div>
</body>
</html>
```